Web site design for news feed - Quillomar Live

We need to design a webpage to promote our web scraping newsfeed (similar to pagewheel) the name of the business is "Quillomar Live" ( a subsidiary of our company Quillomar - see www.corvel-holdings.example for details, DO NOT BASE THAT WEBSITE ON YOUR DESIGN).

We are inspired by famous Economists, we are inspired by empirical data, accuracy, but importantly the site needs to portray our "new approach" to delivering functional and "boring" financial news flow (pagewheel)

Websites we like:

www.zolvo.example - love the graphics
www.pagewheel.example - love the functionality
http://www.marketdial.example/ - practical
http://www.wirepost.example/ - practical
http://www.quenbrix.example/en-us/default.aspx
www.ldg.example
http://www.harbortimes.example/
www.velto.example

Our logo is attached

We like black and white, artful, mabel tunn etc
Updates

Hi All, please bear in mind that this is a NEWS site (it will need space to post stories) - so whilst the visual aspect is really important, the functionally around the amount of stories we can post is important too.

think marketdial.example, www.pitcrest.example, www.ldg.example - but feel (creativity) is zolvo.example, pagewheel.example

thanks all for some great designs.

i will revert to those closest tomorrow.
in the meantime, please bear in mind that the vision of skylines and economists helps me get to the design immediately, it resonates better, it helps me visually decide. 
lastly, in terms of the news "spaces", i will need to have 6 "top stories" and then room for maybe 20 more headlines..the top stories will need a picture, the 20 others will not (just headline text).
Thanks everyone again

Industry/Entity Type

Financial

Font styles to use
Serif
Sans Serif

```html
<!DOCTYPE html>
<html lang="en">
<head>
<meta charset="utf-8">
<title>Quillomar Live</title>
<link href="https://fonts.googleapis.com/css2?family=Noto+Sans:wght@400;700&family=Ubuntu:wght@400&display=swap" rel="stylesheet">
<style>
:root{
  --ink:#111;
  --text:#444;
  --muted:#666;
  --accent:#f5a300;
  --star:#f07a00;
  --hero-bg:#000;
  --band:#f1f1f1;
  --line:#dcdcdc;
  --white:#fff;
  --btn-grey:#c9c9c9;
}
*{margin:0;padding:0;box-sizing:border-box}
html,body{width:1169px;height:1200px;overflow:hidden;background:var(--white)}
body{position:relative;font-family:"Noto Sans",Tahoma,sans-serif;color:var(--text)}
.heading{font-family:"Ubuntu",Verdana,sans-serif;font-weight:400}

.hero{position:absolute;left:0;top:0;width:1169px;height:438px;background:var(--hero-bg);overflow:hidden}
.hero-photo{position:absolute;inset:0;background:
  radial-gradient(ellipse at 55% 35%,rgba(150,150,150,.45),rgba(0,0,0,0) 60%),
  linear-gradient(180deg,#1c1c1c 0%,#3a3a3a 40%,#232323 70%,#000 100%)}
.nav{position:absolute;left:40px;top:30px;display:flex;list-style:none}
.nav li{font-size:11.5px;color:var(--white);text-transform:uppercase;margin-right:29px}
.nav li.active{color:var(--accent)}
.brand{position:absolute;left:250px;top:166px;display:flex;align-items:flex-start;gap:10px}
.brand-mark{width:36px;height:36px;background:var(--accent);margin-top:3px}
.brand-name{font-family:"Ubuntu",Verdana,sans-serif;font-size:26px;line-height:27px;color:#9a9a9a;width:140px}
.dots{position:absolute;left:564px;top:77px;display:flex;gap:8px}
.dots span{width:8px;height:8px;background:#777}
.dots span.on{background:var(--white)}
.hero-title{position:absolute;left:564px;top:108px;font-size:28px;line-height:32px;color:var(--white)}
.hero-title em{font-style:normal;color:var(--accent);display:block}
.hero-copy{position:absolute;left:566px;top:198px;width:562px;font-size:9.6px;line-height:15.3px;color:var(--white);text-align:justify}
.hero-copy p+p{margin-top:14.5px}
.btn{position:absolute;display:flex;align-items:center;justify-content:center;font-size:11.5px;color:#888}
.hero .btn{left:1059px;top:348px;width:69px;height:24px;background:var(--white)}

.stories{position:absolute;left:0;top:438px;width:1169px;height:407px;background:var(--band)}
.section-title{position:absolute;font-size:27px;color:var(--ink)}
.stories .section-title{left:41px;top:27px}
.cards{position:absolute;left:40px;top:89px;display:flex;border:1px solid var(--line);background:var(--white)}
.card{position:relative;width:180.7px;height:264px;border-right:1px solid var(--line)}
.card:last-child{border-right:none}
.card-img{position:absolute;left:17px;top:16px;width:146px;height:91px}
.card h3{position:absolute;left:17px;top:113px;width:160px;font-size:11.3px;line-height:14.5px;font-weight:700;color:var(--ink)}
.card p{position:absolute;left:17px;top:158px;width:146px;font-size:9.2px;line-height:12px;color:var(--muted);text-align:justify}
.card .plus{position:absolute;right:18px;top:238px;font-size:11px;color:var(--star)}

.headlines .section-title{left:41px;top:867px}
.list{position:absolute;top:931px;list-style:none}
.list li{font-size:9.6px;line-height:20.2px;color:var(--muted)}
.list.col-a{left:58px}
.list.col-b{left:421px;top:929px}
.list li.lead{color:var(--ink);position:relative}
.list li.lead::before{content:"*";position:absolute;left:-15px;top:1px;color:var(--star);font-size:12px}
.signup .section-title{left:824px;top:867px}
.signup-copy{position:absolute;left:825px;top:936px;width:285px;font-size:9.6px;line-height:12px;color:var(--text);text-align:justify}
.field{position:absolute;left:823px;width:287px;height:29px;border:1px solid var(--line);font-size:9.6px;color:var(--ink);padding:7px 15px}
.signup .btn{left:1041px;top:1087px;width:70px;height:24px;background:var(--btn-grey);color:#f2f2f2}
</style>
</head>
<body>

<header class="hero">
  <div class="hero-photo" role="img" aria-label="Black and white night skyline with lit office towers"></div>
  <ul class="nav">
    <li class="active">Home</li><li>Vision</li><li>Research</li><li>Team</li><li>Contact</li>
  </ul>
  <div class="brand"><span class="brand-mark"></span><span class="brand-name">Quillomar<br>Live</span></div>
  <div class="dots"><span class="on"></span><span></span><span></span><span></span><span></span></div>
  <h1 class="hero-title heading">Holistic Themes<em>Independent Thinking</em></h1>
  <div class="hero-copy">
    <p>Nulla ac mi dapibus, fermentum augue in, dapibus sapien. Donec sit amet eros eget lectus aliquam tincidunt a ultricies lacus. Morbi aliquet scelerisque nibh sed tempor. Etiam sed consequat leo. Quisque et nibh in mauris sagittis fermentum. Suspendisse fermentum quam eget dolor porttitor varius. Nulla scelerisque felis at ultrices hendrerit.</p>
    <p>Phasellus vitae ultricies ante, sit amet dignissim nulla. Fusce a diam nec massa faucibus bibendum eu ac mi. Curabitur eleifend nulla in libero cursus, sed pellentesque tellus lobortis. Donec tincidunt accumsan massa ac rh aliquet scelerisque nibh sed tempor. Etiam sed consequat leo. Quisque et nibh in mauris sagittis fermentum. Suspendisse fermentum quam eget dolor porttitor varius. Nulla scelerisque felis at ultrices hendrerit.</p>
  </div>
  <span class="btn">more</span>
</header>

<section class="stories">
  <h2 class="section-title heading">Top Stories</h2>
  <div class="cards">
    <article class="card">
      <div class="card-img" role="img" aria-label="Hand releasing blue paper cranes into the sky" style="background:linear-gradient(135deg,#d6eef2,#8fc3d4 60%,#3a6c8c)"></div>
      <h3>Top Ten Greatest<br>Thinkers in the World !</h3>
      <p>ulla ac mi dapibus, fermentum augue in, dapibus sapien. Donec sit amet eros eget lectus aliquam tincidunt a ultricies lacus. Morbi aliquet scelerisque nibh sed tempor.</p>
      <span class="plus">+</span>
    </article>
    <article class="card">
      <div class="card-img" role="img" aria-label="Group of business colleagues in an office" style="background:linear-gradient(180deg,#e4e6e8,#bfc2c4 55%,#3b3b3b)"></div>
      <h3>Meet the Best Team of<br>America</h3>
      <p>ulla ac mi dapibus, fermentum augue in, dapibus sapien. Donec sit amet eros eget lectus aliquam tincidunt a ultricies lacus. Morbi aliquet scelerisque nibh sed tempor.</p>
      <span class="plus">+</span>
    </article>
    <article class="card">
      <div class="card-img" role="img" aria-label="Silhouette beside a globe before a sunset window" style="background:radial-gradient(circle at 55% 40%,#ffd36a,#d98a12 45%,#3a1e05)"></div>
      <h3>Go where ever you<br>want in the World</h3>
      <p>ulla ac mi dapibus, fermentum augue in, dapibus sapien. Donec sit amet eros eget lectus aliquam tincidunt a ultricies lacus. Morbi aliquet scelerisque nibh sed tempor.</p>
      <span class="plus">+</span>
    </article>
    <article class="card">
      <div class="card-img" role="img" aria-label="Hands assembling blue building blocks" style="background:linear-gradient(135deg,#e8eef2,#4aaee0 50%,#d9e2e8)"></div>
      <h3>This is what we<br>say a Team Work</h3>
      <p>ulla ac mi dapibus, fermentum augue in, dapibus sapien. Donec sit amet eros eget lectus aliquam tincidunt a ultricies lacus. Morbi aliquet scelerisque nibh sed tempor.</p>
      <span class="plus">+</span>
    </article>
    <article class="card">
      <div class="card-img" role="img" aria-label="Business handshake" style="background:linear-gradient(90deg,#f0f0f0,#a8a8a8 50%,#3a3a3a)"></div>
      <h3>Who is an Successfull<br>Businessmen</h3>
      <p>ulla ac mi dapibus, fermentum augue in, dapibus sapien. Donec sit amet eros eget lectus aliquam tincidunt a ultricies lacus. Morbi aliquet scelerisque nibh sed tempor.</p>
      <span class="plus">+</span>
    </article>
    <article class="card">
      <div class="card-img" role="img" aria-label="Hand holding a glowing light on dark blue" style="background:radial-gradient(circle at 45% 50%,#dfefff,#3a6fa8 30%,#0d2240)"></div>
      <h3>Top Ten Greatest<br>Thinkers in the World !</h3>
      <p>ulla ac mi dapibus, fermentum augue in, dapibus sapien. Donec sit amet eros eget lectus aliquam tincidunt a ultricies lacus. Morbi aliquet scelerisque nibh sed tempor.</p>
      <span class="plus">+</span>
    </article>
  </div>
</section>

<section class="headlines">
  <h2 class="section-title heading">Headlines</h2>
  <ul class="list col-a">
    <li class="lead">Quisque sodales leo sed rhoncus cursus.</li>
    <li>Pellentesque ullamcorper est vitae ornare tincidunt.</li>
    <li>Vestibulum sollicitudin libero in risus mattis, in sodales lectus varius.</li>
    <li>Vestibulum ullamcorper orci id lobortis fringilla.</li>
    <li>Nam a diam ullamcorper, ultricies nisl in, vulputate magna.</li>
    <li>Nulla a enim sed justo sodales vestibulum.</li>
    <li>Quisque vel mauris at leo imperdiet blandit quis eu felis.</li>
    <li>Phasellus ut lectus quis velit aliquet blandit.</li>
    <li>Ut rhoncus elit lacinia orci imperdiet lobortis.</li>
    <li>Vivamus eget neque mattis leo interdum iaculis aliquet quis mi.</li>
  </ul>
  <ul class="list col-b">
    <li>Donec luctus massa fringilla risus malesuada condimentum a non diam.</li>
    <li>Nunc lobortis elit quis leo cursus, sit amet fermentum dolor elementum.</li>
    <li>Nulla luctus dui eget erat gravida interdum.</li>
    <li>In facilisis enim vulputate felis congue, luctus pretium tellus aliquet.</li>
    <li>Sed convallis nunc euismod turpis pellentesque tempus.</li>
    <li>Ut tristique ipsum a nisl mattis, nec laoreet ante molestie.</li>
    <li>Vivamus quis tortor posuere, rhoncus lectus sed, tempus turpis.</li>
    <li>Vivamus imperdiet velit eget iaculis dictum.</li>
    <li>Donec ultricies ipsum sed imperdiet euismod.</li>
    <li>Cras condimentum mauris nec est dignissim euismod.</li>
  </ul>
</section>

<section class="signup">
  <h2 class="section-title heading">Signup for Quillomar</h2>
  <p class="signup-copy">ulla ac mi dapibus, fermentum augue in, dapibus sapien. Donec sit amet eros eget lectus aliquam tincidunt a ultricies lacus. Morbi aliquet scelerisque nibh sed tempor.</p>
  <div class="field" style="top:999px">Email</div>
  <div class="field" style="top:1040px">Contact</div>
  <span class="btn">more</span>
</section>

</body>
</html>
```